Banner Ad Design Project

This is a banner Ad Design for MindHarbor 2013, a conference and e-Expo in August 2013 to be held at the Larkfield Assembly Hall. The conference's focus is on mental excellence and Brain Health. This conference is bringing together personal and community needs, scientific knowledge, and dedicated professionals to create support and solutions for mental excellence and brain-related health issues. Right now in North America, one out of every two individuals is affected by mental health issues: depression, anxiety, learning disorders, memory loss to name a few.
Who we are:
Organization: Bright Path Foundation
Industry: Non-profit
Target Market(s)
Age group above 18, parents and health professionals, managers.
Industry/Entity Type
Mental Health
Requirements
Must have
- Please follow the warm design grey as in the design samples.
Nice to have
- Buy tickets and ask your unique questions to the medical panel! Seats are limited!

```html
<!DOCTYPE html>
<html lang="en">
<head>
<meta charset="utf-8">
<title>MindHarbor 2013 Banner</title>
<link rel="stylesheet" href="https://fonts.googleapis.com/css2?family=Open+Sans:ital,wght@0,600;0,700;1,700&display=swap">
<style>
  :root {
    --stage: #4a5058;
    --orange-light: #ffa200;
    --orange-deep: #ff6a00;
    --orange-text: #f26a0f;
    --panel-top: #ffffff;
    --panel-bottom: #d9d3ca;
    --grey-text: #4b4b4b;
    --white: #ffffff;
    --brand-red: #d3172b;
  }
  * { margin: 0; padding: 0; box-sizing: border-box; }
  html, body {
    width: 1200px; height: 900px; overflow: hidden;
    background: var(--stage);
    font-family: "Open Sans", Arial, sans-serif;
  }
  .banner {
    position: absolute; left: 162px; top: 395px;
    width: 874px; height: 107px;
    background: linear-gradient(180deg, var(--panel-top) 0%, var(--panel-bottom) 100%);
    overflow: hidden;
  }
  .banner-band { position: absolute; left: 0; top: 0; width: 874px; height: 107px; }
  .event-title {
    position: absolute; left: 17px; top: 6px;
    color: var(--white); font-weight: 700; font-size: 38px; letter-spacing: 0.5px;
    text-shadow: 0 2px 3px rgba(120, 50, 0, 0.45);
  }
  .event-year {
    position: absolute; left: 17px; top: 54px;
    color: var(--white); font-weight: 700; font-style: italic; font-size: 32px;
    text-shadow: 0 2px 3px rgba(120, 50, 0, 0.45);
  }
  .event-venue {
    position: absolute; left: 108px; top: 70px;
    color: var(--white); font-weight: 700; font-size: 16px;
  }
  .tagline {
    position: absolute; left: 394px; top: 9px;
    color: var(--orange-text); font-weight: 700; font-style: italic;
    font-size: 19px; line-height: 24px; text-transform: uppercase;
  }
  .tagline span { display: block; }
  .tagline span + span { padding-left: 11px; }
  .perks {
    position: absolute; left: 422px; top: 73px;
    color: var(--grey-text); font-weight: 600; font-size: 14px;
  }
  .perks .divider { margin: 0 6px; }
  .foundation {
    position: absolute; left: 699px; top: 8px; width: 160px; height: 46px;
    display: flex; align-items: center; gap: 8px;
  }
  .foundation-dot { width: 26px; height: 26px; border-radius: 50%; background: var(--brand-red); flex: none; }
  .foundation-name {
    color: var(--brand-red); font-weight: 700; font-size: 14px; line-height: 16px;
    text-transform: uppercase;
  }
  .buy-tickets {
    position: absolute; left: 698px; top: 68px; width: 153px; height: 29px;
    background: linear-gradient(180deg, var(--orange-light) 0%, var(--orange-deep) 100%);
    color: var(--white); font-weight: 700; font-size: 17px;
    display: flex; align-items: center; justify-content: flex-end; padding-right: 9px;
    text-decoration: none;
  }
  .ticket-icon { position: absolute; left: -4px; top: 0; }
</style>
</head>
<body>
  <div class="banner">
    <svg class="banner-band" viewBox="0 0 874 107" aria-hidden="true">
      <defs>
        <linearGradient id="bandFill" x1="0" y1="0" x2="0" y2="1">
          <stop offset="0" stop-color="#ffa200"/>
          <stop offset="1" stop-color="#ff6a00"/>
        </linearGradient>
      </defs>
      <path d="M0 0 H350 C378 0 384 40 400 70 C412 92 418 102 428 107 H0 Z" fill="url(#bandFill)"/>
    </svg>

    <div class="event-title">MINDHARBOR</div>
    <div class="event-year">2013</div>
    <div class="event-venue">LARKFIELD ASSEMBLY HALL</div>

    <div class="tagline">
      <span>Mental excellence and</span>
      <span>brain health solutions</span>
    </div>
    <div class="perks">LIMITED SEATS<span class="divider">I</span>ASK MEDICAL PANEL</div>

    <div class="foundation">
      <div class="foundation-dot"></div>
      <div class="foundation-name">Bright Path<br>Foundation</div>
    </div>

    <a class="buy-tickets" href="#">
      <svg class="ticket-icon" width="30" height="30" viewBox="0 0 30 30" aria-hidden="true">
        <rect x="5" y="9" width="20" height="12" rx="2" transform="rotate(-35 15 15)" fill="#cfe4f5" stroke="#ffffff" stroke-width="1.5"/>
      </svg>
      BUY TICKETS
    </a>
  </div>
</body>
</html>
```